VORN - Business cards

Business card to be created for Commercial sales staff

Target Market(s)

Commercial businesses

Industry/Entity Type

Commercial

Contact Information for Business Card

Look professional. For commercial clients

Colors
ffffff

Requirements
Must have
• - Vorn Logo
• - Commercial sales staff as postion
• - room for commerical sales manager role
• - person name and their mobile number
• - Website : vornelectrical.com.au
Nice to have
• White background.
• On back of business card just have the logo no other information
Should not have
• Should only have white background on front of card.

```html
<!DOCTYPE html>
<html lang="en">
<head>
<meta charset="utf-8">
<title>VORN – Business Cards</title>
<link href="https://fonts.googleapis.com/css2?family=Lato:wght@400;700;900&display=swap" rel="stylesheet">
<style>
  :root {
    --page-bg: #e9e9e7;
    --card-white: #ffffff;
    --ink: #231f20;
    --accent: #c8202a;
  }
  * { margin: 0; padding: 0; box-sizing: border-box; }
  html, body {
    width: 1200px; height: 1200px; overflow: hidden;
    background: var(--page-bg);
    font-family: 'Lato', sans-serif;
  }
  .sheet {
    position: relative; width: 1200px; height: 1200px;
    display: flex; flex-direction: column; align-items: center; justify-content: center; gap: 60px;
  }
  .card {
    position: relative; width: 900px; height: 514px;
    background: var(--card-white);
    box-shadow: 0 6px 24px rgba(0,0,0,0.12);
    overflow: hidden;
  }

  /* Back: logo side */
  .card-back .brand-band {
    position: absolute; left: 0; top: 200px; width: 270px; height: 150px;
    background: var(--ink);
  }
  .card-back .brand-name {
    position: absolute; left: 330px; top: 227px;
    display: flex; align-items: center; gap: 18px;
  }
  .brand-name .brand-dot {
    width: 22px; height: 22px; border-radius: 50%; background: var(--accent);
  }
  .brand-name .brand-word {
    font-size: 96px; font-weight: 900; letter-spacing: 4px; color: var(--ink); line-height: 1;
  }

  /* Front: contact side */
  .card-front .bracket { position: absolute; }
  .card-front .bracket-open { left: 60px; top: 130px; width: 60px; height: 170px; }
  .card-front .bracket-close { left: 395px; top: 280px; width: 60px; height: 150px; }
  .card-front .person {
    position: absolute; left: 110px; top: 180px;
  }
  .person .person-name {
    font-size: 34px; font-weight: 900; letter-spacing: 1px; color: var(--ink);
  }
  .person .person-role {
    margin-top: 8px; font-size: 19px; font-weight: 400; letter-spacing: 1.5px; color: var(--ink);
  }
  .card-front .contact-band {
    position: absolute; left: 470px; top: 300px; width: 430px; height: 150px;
    background: var(--ink); color: var(--card-white);
    padding: 26px 28px; display: grid; grid-template-columns: 90px 1fr; row-gap: 8px;
    font-size: 19px; align-content: center;
  }
  .contact-band .contact-label { font-weight: 400; }
  .contact-band .contact-value { font-weight: 400; letter-spacing: 0.5px; white-space: nowrap; }
</style>
</head>
<body>
<main class="sheet">

  <section class="card card-back" aria-label="Business card back">
    <div class="brand-band"></div>
    <div class="brand-name">
      <span class="brand-dot"></span>
      <span class="brand-word">VORN</span>
    </div>
  </section>

  <section class="card card-front" aria-label="Business card front">
    <svg class="bracket bracket-open" viewBox="0 0 60 170" aria-hidden="true">
      <polyline points="55,4 8,4 8,166 30,166" fill="none" stroke="#231f20" stroke-width="7"/>
    </svg>
    <div class="person">
      <p class="person-name">ALEX REED MORGAN</p>
      <p class="person-role">COMMERCIAL SALES MANAGER</p>
    </div>
    <svg class="bracket bracket-close" viewBox="0 0 60 150" aria-hidden="true">
      <polyline points="30,4 52,4 52,146 5,146" fill="none" stroke="#231f20" stroke-width="7"/>
    </svg>
    <div class="contact-band">
      <span class="contact-label">phone</span><span class="contact-value">: 000 . PHONE . NO.</span>
      <span class="contact-label">email</span><span class="contact-value">: www@vornelectrical.com.au</span>
      <span class="contact-label">website</span><span class="contact-value">: www.vornelectrical.com.au</span>
    </div>
  </section>

</main>
</body>
</html>
```